Ordinary Velvet Sparrow inquiring into the Mystery of her Heart needs a Book Cover design

Hello! I need a book cover design (for printed softcover 6” x 9” and eBook) for my new book titled "The Wide Season of a Modest Velvet Sparrow: Notes on Finding Room for Every Part." It's the story of a mom juggling a demanding technology career who embarks upon a self-discovery journey, faces cancer, and learns to expand her life, one vulnerable nibble at a time. With the help of a guide on her spiritual path, she learns to let go of her strong woman do-it-all persona, allowing her soul to fully shine. My purpose in writing the book is to share what I've learned about finding the "moreness" in being human.
*I would like to see book cover designs that communicate a sense of both strength and vulnerability, confidence and humbleness, curiosity and inner discovery—hinting at what's to come. I’ve uploaded a few images that I like because they feel clean and simple, and because they can be interpreted as metaphors of the beauty and power within each of us.
*If your design submission includes a mirror reflection of some sort of a “velvet sparrow” image that people are familiar with, then I would like it to convey a reluctant or questioning velvet sparrow, rather than a bold, fighting-to-save-the-world velvet sparrow.
*I lean toward a clean and calming background, as the book is really an inquiry into the mystery of this heart. It’s an examination of what I might have lost of myself, and ultimately gained, through all my crazy years of juggling. So, it’s a journey of spiritual growth.
Thank you for your interest and sharing your creative talent.

Target Market(s)

(1) Career-oriented parents, especially moms, who are in their 30's and 40's, in the midst of the struggle of trying to juggle it all; (2) life-long strivers, age 55+, who are finally slowing down and looking back to try and make sense of their lives, seeking to understand their buried inner life

Industry/Entity Type

Book Categories: Women & Business; Spiritual Self-help; Strong Women

Font styles to use
Serif

Colors

Designer to choose colors to be used in the design.

Requirements
Must have
• Clean and simple overall feeling
Nice to have
• I am open to including color—if so, perhaps some (not too much) hunter green would be nice (not required, but I’ve used it in a draft website design and rather like it).
Should not have
• Should not feel too "busy"

```html
<!DOCTYPE html>
<html lang="en">
<head>
<meta charset="utf-8">
<title>The Wide Season of a Modest Velvet Sparrow — Book Cover</title>
<link rel="stylesheet" href="https://fonts.googleapis.com/css2?family=Crimson+Text:ital,wght@0,400;1,400&family=Montserrat:wght@400;500&display=swap">
<style>
  :root {
    --backdrop: #1b2830;
    --paper: #ffffff;
    --ink: #111111;
    --accent: #d7282f;
    --rule: #c9c9c9;
    --art-edge: rgba(255, 255, 255, 0);
    --art-mid: #ededed;
    --art-core: #f3c9c9;
  }
  * { margin: 0; padding: 0; box-sizing: border-box; }
  html, body {
    width: 1200px;
    height: 1200px;
    overflow: hidden;
    background: var(--backdrop);
  }
  .cover {
    position: absolute;
    left: 240px;
    top: 60px;
    width: 720px;
    height: 1080px;
    background: var(--paper);
    color: var(--ink);
  }
  .cover-art {
    position: absolute;
    left: 238px;
    top: 57px;
    width: 244px;
    height: 386px;
    background:
      radial-gradient(circle at 50% 72%, var(--art-core) 0%, rgba(243, 201, 201, 0) 22%),
      radial-gradient(ellipse at 50% 50%, var(--art-mid) 0%, var(--art-mid) 40%, var(--art-edge) 72%);
  }
  .title { font-weight: 400; }
  .line {
    position: absolute;
    left: 0;
    width: 100%;
    text-align: center;
    line-height: 1;
    white-space: nowrap;
  }
  .line--serif {
    font-family: "Crimson Text", Georgia, serif;
    font-style: italic;
    font-weight: 400;
    font-size: 58px;
    color: var(--ink);
  }
  .line--display {
    font-family: "Montserrat", Arial, sans-serif;
    font-weight: 400;
    font-size: 72px;
    color: var(--accent);
    letter-spacing: 0.005em;
  }
  .title-the      { top: 456px; }
  .title-season   { top: 512px; }
  .title-modest   { top: 580px; }
  .title-velvet   { top: 651px; }
  .title-sparrow  { top: 724px; }

  .divider {
    position: absolute;
    left: 222px;
    width: 276px;
    height: 1px;
    background: var(--rule);
  }
  .divider--top { top: 832px; }
  .divider--bottom { top: 928px; }

  .subtitle {
    position: absolute;
    left: 0;
    top: 840px;
    width: 100%;
    text-align: center;
    font-family: "Crimson Text", Georgia, serif;
    font-style: italic;
    font-weight: 400;
    font-size: 33px;
    line-height: 38px;
    color: var(--ink);
  }
  .subtitle .highlight { color: var(--accent); }

  .author {
    position: absolute;
    left: 0;
    top: 1004px;
    width: 100%;
    text-align: center;
    font-family: "Montserrat", Arial, sans-serif;
    font-weight: 400;
    font-size: 29px;
    line-height: 1;
    letter-spacing: 0.32em;
    padding-left: 0.32em;
    color: var(--ink);
  }
</style>
</head>
<body>
  <main class="cover">
    <div class="cover-art" role="img" aria-label="Black line illustration of a figure with flowers growing from an open head, hands held over a glowing red heart"></div>

    <h1 class="title">
      <span class="line line--serif title-the">The</span>
      <span class="line line--display title-season">WIDE SEASON</span>
      <span class="line line--serif title-modest">of a modest</span>
      <span class="line line--display title-velvet">VELVET</span>
      <span class="line line--display title-sparrow">SPARROW</span>
    </h1>

    <div class="divider divider--top"></div>
    <p class="subtitle">Notes on<br>Finding <span class="highlight">Room</span> for Every Part</p>
    <div class="divider divider--bottom"></div>

    <p class="author">AUTHOR NAME</p>
  </main>
</body>
</html>
```